Redesign website for Sunny Casas

Sunny Casas Algarve (www.sunnycasasalgarve-example.com) is a vacation rental company based in Algarve, Portugal.
We want to redesign our website for a more modern and responsive version.

We do like something like this: https://www.plushhideaways-example.com, https://www.tidalkeyhomes-example.com, http://www.moraspropertyqx-example.com, and https://www.kelvatrum-example.com

We would prefer the use of a Wordpress theme specific for vacation rentals, that already has the tools that we need: reservations, availability sync via Ical, and payments.

Target Market(s)

The website must be appealing to guests who book directly, and to property owners, who deliver their villas to our portfolio.

Industry/Entity Type

Accommodation

Coding

Coded - Design and coding required

Font styles to use
Sans Serif

Colors
33a6d7
85cae6
cee9f5
cfeae6
86cfc6

Requirements
Must have
• A summery and holiday look

```html
<!DOCTYPE html>
<html lang="en">
<head>
<meta charset="utf-8">
<title>Sunny Casas – The Algarve holiday collection</title>
<link rel="stylesheet" href="https://fonts.googleapis.com/css2?family=Open+Sans:wght@400;600;700&family=Oswald:wght@400;500&family=Roboto+Condensed:wght@400;700&display=swap">
<style>
:root{
  --blue:#33a6d7;
  --blue-light:#85cae6;
  --blue-pale:#cee9f5;
  --teal-pale:#cfeae6;
  --teal:#86cfc6;
  --navy:#1f4f73;
  --ink:#222;
  --grey:#666;
  --band:#f4f4f4;
  --footer:#121212;
  --white:#fff;
}
*{margin:0;padding:0;box-sizing:border-box}
html,body{width:1200px;height:3346px;overflow:hidden}
body{position:relative;background:var(--white);font-family:"Open Sans",sans-serif;color:var(--ink)}
.abs{position:absolute}
/* header */
.topbar{left:758px;top:0;width:357px;height:34px;background:var(--blue);border-radius:0 0 0 16px;color:var(--white);font-size:13px;display:flex;align-items:center;gap:8px;padding-left:28px}
.flag{width:16px;height:16px;border-radius:50%;display:inline-block}
.header-line{left:0;top:0;width:1200px;height:4px;background:var(--blue)}
.logo{left:85px;top:40px;font-weight:400;font-size:34px;letter-spacing:2px;color:var(--blue-light)}
.nav{left:448px;top:58px;display:flex;gap:41px;font-size:15.5px;color:var(--ink)}
.nav .active{color:var(--blue)}
/* hero */
.hero{left:0;top:112px;width:1200px;height:539px;background:linear-gradient(180deg,#27466e 0%,#6d6a5a 45%,#3a3b36 75%,#1e2a34 100%)}
.hero-title{left:0;top:304px;width:1200px;text-align:center;font-family:"Oswald",sans-serif;font-weight:400;color:var(--white);font-size:54px;line-height:1;letter-spacing:0}
.hero-sub{left:0;top:372px;width:1200px;text-align:center;font-family:"Oswald",sans-serif;color:var(--white);font-size:46px;font-weight:400}
.hero-arrow{top:372px;color:var(--white);font-size:18px}
.search{left:87px;top:575px;width:1021px;height:143px;background:var(--blue);box-shadow:0 8px 24px rgba(0,0,0,.18)}
.field-label{color:var(--white);font-size:15px;top:32px}
.field{top:64px;height:48px;background:var(--white);border-radius:2px;font-size:15px;padding:14px;color:var(--ink)}
.search-btn{left:815px;top:64px;width:143px;height:48px;background:var(--navy);color:var(--white);font-size:16px;text-align:center;line-height:48px;border-radius:2px}
/* welcome */
.h2{font-family:"Roboto Condensed",sans-serif;font-weight:400;font-size:34px;color:var(--ink);text-align:center;width:1200px;left:0}
.intro{left:140px;top:855px;width:920px;text-align:center;font-size:13.5px;line-height:25px;color:var(--grey)}
.feature{width:180px;text-align:center;top:984px}
.feature .ring{width:118px;height:118px;border-radius:50%;margin:0 auto;background:var(--teal);border:6px solid var(--teal-pale);display:flex;align-items:center;justify-content:center}
.feature p{margin-top:6px;font-size:15.5px;color:var(--ink)}
/* holiday rentals */
.rentals{left:0;top:1233px;width:1200px;height:529px;background:linear-gradient(180deg,#2b4f7e 0%,#5f7f6a 40%,#1b5ea8 70%,#0e3d86 100%)}
.rentals-title{left:87px;top:1292px;font-family:"Roboto Condensed",sans-serif;font-weight:400;color:var(--white);font-size:34px}
.play{width:52px;height:52px;border-radius:50%;border:3px solid var(--white);background:rgba(0,0,0,.35)}
.caption{left:87px;top:1597px;width:383px;height:78px;background:rgba(10,25,45,.75);color:var(--white);padding:14px 18px}
.caption b{font-size:20px;font-weight:600;display:block}
.caption span{font-size:15px}
.slide-nav{top:1688px;width:26px;height:26px;border-radius:50%;background:rgba(255,255,255,.35);color:var(--white);text-align:center;line-height:26px;font-size:13px}
.thumb-text{right:288px;text-align:right;color:var(--white);width:220px}
.thumb-text .kicker{font-size:12px;opacity:.9}
.thumb-text .name{font-size:16px;font-weight:700;margin:3px 0}
.thumb-text .desc{font-size:12.5px;line-height:20px;opacity:.9}
.thumb{left:932px;width:178px}
/* villas */
.card-img{width:308px;height:205px}
.card-kicker{font-size:13px;color:var(--blue)}
.card-title{font-size:17.5px;color:var(--ink)}
/* reviews */
.reviews{left:0;top:2591px;width:1200px;height:424px;background:var(--band)}
.quote{left:195px;top:2736px;width:810px;text-align:center;font-size:13.5px;line-height:24.5px;color:var(--grey)}
.qmark{color:var(--blue);font-family:Georgia,serif;font-size:30px;font-weight:700;line-height:0;vertical-align:-4px}
.avatar{left:553px;top:2827px;width:94px;height:94px;border-radius:50%;background:linear-gradient(160deg,#c9a58a,#6d7f93);border:4px solid var(--white)}
.rev-arrow{top:2855px;color:#999;font-size:30px}
.rev-name{left:0;top:2937px;width:1200px;text-align:center;font-size:14px;font-style:italic;color:var(--ink)}
/* footer */
.footer{left:0;top:3015px;width:1200px;height:331px;background:var(--footer)}
.footer-logo{left:87px;top:3152px;color:var(--white);font-size:24px;letter-spacing:2px}
.fcol{top:3084px;color:var(--white)}
.fcol h4{font-weight:400;font-size:17px;margin-bottom:16px}
.fcol li{list-style:none;font-size:12.5px;line-height:23.5px}
.fcol li::before{content:"» "}
.contact li::before{content:none}
.contact li{display:flex;align-items:center;gap:8px}
.footer-rule{left:87px;top:3245px;width:1023px;height:1px;background:#333}
.copyright{left:95px;top:3282px;color:var(--white);font-size:12.5px}
.social{top:3275px;width:26px;height:26px;background:var(--white);border-radius:4px}
</style>
</head>
<body>

<header>
  <div class="abs header-line"></div>
  <div class="abs topbar">
    <svg width="13" height="13" viewBox="0 0 24 24"><path fill="#fff" d="M6.6 10.8a15 15 0 0 0 6.6 6.6l2.2-2.2c.3-.3.7-.4 1-.2 1.1.4 2.3.6 3.6.6.6 0 1 .4 1 1V20c0 .6-.4 1-1 1A17 17 0 0 1 3 4c0-.6.4-1 1-1h3.5c.6 0 1 .4 1 1 0 1.3.2 2.5.6 3.6.1.3 0 .7-.2 1z"/></svg>
    <span>+351 289 000 147 |</span>
    <span class="flag" style="background:linear-gradient(90deg,#1d7a3a 40%,#d4232b 40%)"></span>
    <span class="flag" style="background:linear-gradient(90deg,#23408e 33%,#fff 33%,#fff 66%,#e23b3b 66%)"></span>
    <span class="flag" style="background:#27407e;border:2px solid #c8283b"></span>
  </div>
  <div class="abs logo">SUNNY CASAS</div>
  <nav class="abs nav">
    <span class="active">Home</span><span>Holiday Rentals</span><span>What to Do</span><span>Guest Services</span><span>Reviews</span><span>Contact</span>
  </nav>
</header>

<section>
  <div class="abs hero" role="img" aria-label="Photo of a lit villa with swimming pool and sun loungers at dusk"></div>
  <div class="abs hero-arrow" style="left:72px">‹</div>
  <div class="abs hero-arrow" style="left:1108px">›</div>
  <h1 class="abs hero-title">SUNNY CASAS</h1>
  <p class="abs hero-sub">The Algarve holiday collection</p>

  <form class="abs search">
    <span class="abs field-label" style="left:57px">Check In</span>
    <span class="abs field-label" style="left:299px">Check Out</span>
    <span class="abs field-label" style="left:535px">Adults</span>
    <span class="abs field-label" style="left:676px">Kids</span>
    <div class="abs field" style="left:57px;width:212px"><svg class="abs" style="right:14px;top:17px" width="13" height="13" viewBox="0 0 13 13"><rect x="1" y="2" width="11" height="10" fill="none" stroke="#555"/><rect x="1" y="2" width="11" height="3" fill="#555"/></svg></div>
    <div class="abs field" style="left:299px;width:212px"><svg class="abs" style="right:14px;top:17px" width="13" height="13" viewBox="0 0 13 13"><rect x="1" y="2" width="11" height="10" fill="none" stroke="#555"/><rect x="1" y="2" width="11" height="3" fill="#555"/></svg></div>
    <div class="abs field" style="left:535px;width:110px">1</div>
    <div class="abs field" style="left:676px;width:110px">0</div>
    <div class="abs search-btn">SEARCH</div>
  </form>
</section>

<section>
  <h2 class="abs h2" style="top:792px">Welcome To Sunny Casas</h2>
  <p class="abs intro">We think style may be also accessible, so we choose really cool houses in our naturally beautiful Algarve just for you...<br>With us you can experience not only stylish villas, but also family retreats at their very best. In the Algarve the beach is stunning, the enter-<br>tainment and restaurants incredible, the golf courses amazing. All of that plus the option to enjoy our cool services &amp; activities!</p>

  <div class="abs feature" style="left:113px"><div class="ring"><svg width="48" height="40" viewBox="0 0 48 40" fill="none" stroke="#fff" stroke-width="4" stroke-linecap="round"><path d="M4 14a28 28 0 0 1 40 0"/><path d="M11 21a18 18 0 0 1 26 0"/><path d="M18 28a8 8 0 0 1 12 0"/><circle cx="24" cy="35" r="2" fill="#fff"/></svg></div><p>WiFi</p></div>
  <div class="abs feature" style="left:302px"><div class="ring"><svg width="40" height="50" viewBox="0 0 40 50" fill="#fff"><path d="M10 4h20l6 22H4z"/><rect x="18" y="26" width="4" height="16"/><rect x="10" y="42" width="20" height="4"/></svg></div><p>Fully Furnished</p></div>
  <div class="abs feature" style="left:501px"><div class="ring"><svg width="40" height="48" viewBox="0 0 40 48"><text x="20" y="42" text-anchor="middle" font-family="Open Sans,sans-serif" font-weight="700" font-size="46" fill="#fff">P</text></svg></div><p>Free Parking</p></div>
  <div class="abs feature" style="left:708px"><div class="ring"><svg width="46" height="46" viewBox="0 0 24 24" fill="#fff"><path d="M21 16v-2l-8-5V3.5a1.5 1.5 0 0 0-3 0V9l-8 5v2l8-2.5V19l-2 1.5V22l3.5-1 3.5 1v-1.5L13 19v-5.5z" transform="rotate(45 12 12)"/></svg></div><p>Airport Transfers</p></div>
  <div class="abs feature" style="left:909px"><div class="ring"><svg width="46" height="46" viewBox="0 0 46 46" fill="none" stroke="#fff" stroke-width="3.5" stroke-linecap="round"><path d="M40 4L24 22"/><path d="M20 18l10 10-6 12c-6-2-14-8-18-16z" fill="#fff"/></svg></div><p>Cleaning Services</p></div>
</section>

<section>
  <div class="abs rentals" role="img" aria-label="Photo of a resort swimming pool surrounded by whitewashed villas"></div>
  <h2 class="abs rentals-title">Holiday Rentals</h2>
  <div class="abs play" style="left:573px;top:1469px"><svg width="46" height="46" viewBox="0 0 46 46"><path d="M18 14l13 9-13 9z" fill="#fff"/></svg></div>
  <div class="abs caption"><b>Neque porro quisquam est qui</b><span>quisquam est qui dolorem quia dolor sit amet,</span></div>
  <div class="abs slide-nav" style="left:87px">‹</div>
  <div class="abs slide-nav" style="left:119px">›</div>

  <div class="abs thumb-text" style="top:1303px"><div class="kicker">Porro quisquam</div><div class="name">Faro &amp; Ria Formosa</div><div class="desc">It is long established fact a<br>reader will be distracted</div></div>
  <div class="abs thumb-text" style="top:1453px"><div class="kicker">Porro quisquam</div><div class="name">Tavira, Cacela</div><div class="desc">It is long established fact a<br>reader will be distracted</div></div>
  <div class="abs thumb-text" style="top:1603px"><div class="kicker">Porro quisquam</div><div class="name">ipsum quia dolor est</div><div class="desc">It is long established fact a<br>reader will be distracted</div></div>

  <div class="abs thumb" style="top:1287px;height:133px;background:linear-gradient(160deg,#8fb4d9,#b9a58c)" role="img" aria-label="Photo of a historic church in Faro"></div>
  <div class="abs thumb" style="top:1438px;height:130px;background:linear-gradient(160deg,#1f5fa8,#d9dde3)" role="img" aria-label="Photo of a white chimney against a blue sky in Tavira"></div>
  <div class="abs thumb" style="top:1586px;height:124px;background:linear-gradient(180deg,#9cc3df,#5d87a5)" role="img" aria-label="Photo of a small fishing boat on calm water"></div>
  <div class="abs play" style="left:1006px;top:1338px;width:28px;height:28px;border-width:2px"><svg width="24" height="24" viewBox="0 0 24 24"><path d="M9 7l7 5-7 5z" fill="#fff"/></svg></div>
  <div class="abs play" style="left:1006px;top:1489px;width:28px;height:28px;border-width:2px"><svg width="24" height="24" viewBox="0 0 24 24"><path d="M9 7l7 5-7 5z" fill="#fff"/></svg></div>
  <div class="abs play" style="left:1006px;top:1634px;width:28px;height:28px;border-width:2px"><svg width="24" height="24" viewBox="0 0 24 24"><path d="M9 7l7 5-7 5z" fill="#fff"/></svg></div>
</section>

<section>
  <h2 class="abs h2" style="top:1838px">Villas &amp; Apartments</h2>

  <div class="abs card-img" style="left:100px;top:1929px;background:linear-gradient(170deg,#6f9f4d,#c7a47c)" role="img" aria-label="Photo of a garden dining table beside a pool"></div>
  <div class="abs card-img" style="left:444px;top:1929px;background:linear-gradient(170deg,#e6ddce,#7a4a2e)" role="img" aria-label="Photo of a living room with sofas and fireplace"></div>
  <div class="abs card-img" style="left:787px;top:1929px;background:linear-gradient(170deg,#bcd8ea,#8e5a34)" role="img" aria-label="Photo of a terrace dining table with sea view"></div>
  <div class="abs card-kicker" style="left:105px;top:2146px">Porro Quisquam</div>
  <div class="abs card-kicker" style="left:449px;top:2146px">Porro Quisquam</div>
  <div class="abs card-kicker" style="left:792px;top:2146px">Porro Quisquam</div>
  <div class="abs card-title" style="left:105px;top:2168px">Dolorem ipsum quia</div>
  <div class="abs card-title" style="left:449px;top:2168px">Neque porro quisquam</div>
  <div class="abs card-title" style="left:792px;top:2168px">Quisquam est dolorem</div>

  <div class="abs card-img" style="left:100px;top:2239px;background:linear-gradient(170deg,#e9e4dc,#8a857d)" role="img" aria-label="Photo of a bright lounge with armchair and coffee table"></div>
  <div class="abs card-img" style="left:444px;top:2239px;background:linear-gradient(180deg,#3f8fd6,#e8eef2 45%,#4cb6e0 75%,#6aa14a)" role="img" aria-label="Photo of an apartment building with a large pool"></div>
  <div class="abs card-img" style="left:787px;top:2239px;background:linear-gradient(170deg,#8aa05a,#5b4a38)" role="img" aria-label="Photo of a shaded pergola dining area in a garden"></div>
  <div class="abs card-kicker" style="left:105px;top:2456px">Porro Quisquam</div>
  <div class="abs card-kicker" style="left:449px;top:2456px">Porro Quisquam</div>
  <div class="abs card-kicker" style="left:792px;top:2456px">Porro Quisquam</div>
  <div class="abs card-title" style="left:105px;top:2478px">Dolorem ipsum quia</div>
  <div class="abs card-title" style="left:449px;top:2478px">Neque porro quisquam</div>
  <div class="abs card-title" style="left:792px;top:2478px">Quisquam est dolorem</div>
</section>

<section>
  <div class="abs reviews"></div>
  <h2 class="abs h2" style="top:2658px">Reviews</h2>
  <p class="abs quote"><span class="qmark">“</span>&nbsp; It has survived not only five centuries, but also the leap into electronic typesetting, remaining essentially unchanged. It was popularised in the 1960s with the release of Kelnor sheets containing Lorem Ipsum passages, and more recently with desktop publishing software like Pagewright Studio including versions of Lorem Ipsum &nbsp;<span class="qmark">”</span></p>
  <div class="abs rev-arrow" style="left:508px">‹</div>
  <div class="abs avatar" role="img" aria-label="Reviewer portrait"></div>
  <div class="abs rev-arrow" style="left:672px">›</div>
  <p class="abs rev-name">Neque porro quisquam</p>
</section>

<footer>
  <div class="abs footer"></div>
  <div class="abs footer-logo">SUNNY CASAS</div>
  <div class="abs fcol" style="left:350px"><h4>Links</h4><ul><li>About Us</li><li>Terms &amp; Conditions</li><li>List your Property</li><li>Buy a Rental Property</li></ul></div>
  <div class="abs fcol" style="left:546px"><h4>Links 2</h4><ul><li>Rent a Car</li><li>Contact Us</li><li>Dolorem</li><li>Quisquam</li></ul></div>
  <div class="abs fcol" style="left:722px"><h4>Quicklink</h4><ul><li>Consectetur</li><li>Dolorem</li><li>Neque porro</li><li>Ipsum quia</li></ul></div>
  <div class="abs fcol contact" style="left:903px"><h4>Contact</h4><ul>
    <li><svg width="11" height="12" viewBox="0 0 24 24"><path fill="#fff" d="M12 2a7 7 0 0 0-7 7c0 5 7 13 7 13s7-8 7-13a7 7 0 0 0-7-7zm0 9.5A2.5 2.5 0 1 1 12 6.5a2.5 2.5 0 0 1 0 5z"/></svg>27 Rua das Palmeiras, Lagos 8600</li>
    <li><svg width="11" height="12" viewBox="0 0 24 24"><path fill="#fff" d="M6.6 10.8a15 15 0 0 0 6.6 6.6l2.2-2.2c.3-.3.7-.4 1-.2 1.1.4 2.3.6 3.6.6.6 0 1 .4 1 1V20c0 .6-.4 1-1 1A17 17 0 0 1 3 4c0-.6.4-1 1-1h3.5c.6 0 1 .4 1 1 0 1.3.2 2.5.6 3.6.1.3 0 .7-.2 1z"/></svg>(289) 555-0147</li>
    <li><svg width="11" height="12" viewBox="0 0 24 24"><path fill="#fff" d="M2 5h20v14H2z"/><path d="M2 5l10 8 10-8" fill="none" stroke="#121212" stroke-width="2"/></svg>hello@sunnycasas-example.com</li>
  </ul></div>
  <div class="abs footer-rule"></div>
  <div class="abs copyright">Copyright © 2018, All Rights Reserved</div>
  <div class="abs social" style="left:968px"></div>
  <div class="abs social" style="left:1005px"></div>
  <div class="abs social" style="left:1042px"></div>
  <div class="abs social" style="left:1079px"></div>
</footer>

</body>
</html>
```